Banner Ad Design Project

**Outdoor Banners required for Retail Shop**
Deadline - Final Approved Concepts required to send off to the printers on Monday 16th July, 12noon Eastern Standard Time Australia.
4 Outdoor Signs Designs:
**Please note all signs need to capture the attention of possible customers driving past - so clear easy to read & eye catching content. Please see below for details and content guides on each sign.**
Artwork Required
- Review/Rework - Once 6 X 1.5 metre Mesh Banner (i have design concept done up - need a review & re-work of exisiting concept)Single Side Print
- Create - One 4 x 1 metre Vinal Banner, Single Side Print
- Create - Two 3.5 metre Bow Flags (both flags will be double sided print)
What is provided to you (files attached):
- Artwork Requirements from the printer
- Artwork Layout Base Templates for each item as per printers request
- Some existing artwork concepts in use and ideas
- Wording that needs to be incorporated
- Hi Res Logo
What else might be required
- pictures of some sort?
MESH BANNER (6m x 1m)
Pls use artwork template provided that has been setup with eyelets and design space available. File is brambo6x1meshbanner.pdf)
- Single Sided Print
- Mesh material has micro-holes is very useful for construction site and building enclosures, or a promotional banner which needs to let some light and/or breeze through
- pls make sure your design will be readable on a mesh material banner
- We will be placing on a wire fence
- Viewing distance: 5m
- Content to incorporate info from example design file attached brambo6x1.pdf
- *Can also consider incorporating the text "Direct To the Public" and any of the content ideas below.
Bow Wind Flags (3.5m)
We need 2 Bow Flags done. Both will be double sided print (Each flag needs a side(a) and side(b) file as per below. These flags will be placed in front of the shop by the road to capture attention of people driving by.
Flag 1 Content - Focus on Pest Type
Content can include/capture following ideas:
- Branding/Logo
- DIY Do it Yourself
- Cockroaches
- Ants
- Rats & Mice
- Wasps
- Fly Control
- Termites
Flag 2 Content - Focus on What we Sell
- Branding/Logo
- DIY Do it Yourself
- Pest Control Products
- Professional Brands
Vinal Banner (4m x 1m)
Can include a mixture of any content previous provided.
Will be located on by the Front Door Entrance.
An example of a 3x1 banner we had done up is attached as an idea.
- Branding/Logo
- DIY Do it Yourself
- Pictures
- Professional Pest Control Products
- www.brambo.com.au
- Ph: 4917 3604
- Shop Online & Instore
Updates
Hi Designers
Target Market(s)
Potential Customers driving past our new retail store on a main road which can include:
- General Australian Public
- Business Owners/Maintenance Staff that look after pest control for a business
Industry/Entity Type
Construction
Requirements
Must have
- Clear and Easy to Read!
People will be driving past on a main road so they will not have a lot of time to view the signs. They must capture attention quickly
Consistency - all banners must incorporate our logo and DIY box
Should not have
- Too much content - please use our content ideas as options but make sure the banners are not cluttered.

```html
<!DOCTYPE html>
<html lang="en">
<head>
<meta charset="utf-8">
<title>Brambo Mesh Banner</title>
<link href="https://fonts.googleapis.com/css2?family=Open+Sans:wght@700&family=Arimo:wght@700&display=swap" rel="stylesheet">
<style>
  :root {
    --brand-green: #1f8a45;
    --bright-green: #7cbf3f;
    --pillar-dark: #0c4a22;
    --pillar-light: #2fae52;
    --panel-black: #040504;
    --white: #ffffff;
    --card-border: #c9c9c9;
  }
  html, body {
    margin: 0;
    width: 1200px;
    height: 800px;
    overflow: hidden;
    background: var(--white);
  }
  .canvas {
    position: relative;
    width: 1200px;
    height: 800px;
  }
  .banner {
    position: absolute;
    left: 22px;
    top: 250px;
    width: 1156px;
    height: 302px;
    background: var(--panel-black);
  }
  .ticker {
    position: absolute;
    left: 0;
    width: 100%;
    height: 41px;
    background: var(--brand-green);
    color: var(--white);
    font-family: "Arimo", Arial, sans-serif;
    font-weight: 700;
    font-size: 21.5px;
    line-height: 41px;
    text-align: center;
    white-space: nowrap;
  }
  .ticker--top { top: 0; }
  .ticker--bottom { bottom: 0; height: 40px; line-height: 40px; }
  .pillar {
    position: absolute;
    top: 41px;
    width: 100px;
    height: 221px;
    background: linear-gradient(90deg, var(--pillar-dark), var(--pillar-light) 45%, var(--pillar-dark));
  }
  .pillar--left { left: 28px; }
  .pillar--right { right: 28px; }
  .brand-card {
    position: absolute;
    top: 68px;
    width: 136px;
    height: 168px;
    background: var(--white);
    border: 2px solid var(--card-border);
    box-sizing: border-box;
    border-radius: 3px;
  }
  .brand-card--left { left: 23px; }
  .brand-card--right { right: 20px; }
  .brand-square {
    position: absolute;
    left: 32px;
    top: 18px;
    width: 68px;
    height: 68px;
    background: var(--brand-green);
  }
  .brand-name {
    position: absolute;
    left: 0;
    right: 0;
    top: 104px;
    text-align: center;
    color: var(--brand-green);
    font-family: "Open Sans", Arial, sans-serif;
    font-weight: 700;
    font-size: 28px;
    line-height: 1.1;
  }
  .message {
    position: absolute;
    left: 0;
    right: 0;
    text-align: center;
    font-family: "Open Sans", Arial, sans-serif;
    font-weight: 700;
    line-height: 1;
    white-space: nowrap;
  }
  .headline {
    top: 56px;
    font-size: 68px;
    color: var(--white);
    letter-spacing: -0.5px;
  }
  .subline {
    top: 126px;
    font-size: 37px;
    color: var(--bright-green);
    letter-spacing: -0.5px;
  }
  .phone {
    top: 166px;
    font-size: 86px;
    color: var(--white);
    margin-left: -12px;
  }
</style>
</head>
<body>
<div class="canvas">
  <section class="banner">
    <div class="ticker ticker--top">SHOP INSTORE &amp; ONLINE - WWW.BRAMBO.COM.AU - SHOP INSTORE &amp; ONLINE - WWW.BRAMBO.COM.AU</div>

    <div class="pillar pillar--left"></div>
    <div class="pillar pillar--right"></div>

    <div class="brand-card brand-card--left">
      <div class="brand-square"></div>
      <div class="brand-name">Brambo</div>
    </div>

    <div class="message headline">Control Pests Yourself</div>
    <div class="message subline">THE PROFESSIONAL WAY</div>
    <div class="message phone">4917 3604</div>

    <div class="brand-card brand-card--right">
      <div class="brand-square"></div>
      <div class="brand-name">Brambo</div>
    </div>

    <div class="ticker ticker--bottom">SHOP INSTORE &amp; ONLINE - WWW.BRAMBO.COM.AU - SHOP INSTORE &amp; ONLINE - WWW.BRAMBO.COM.AU</div>
  </section>
</div>
</body>
</html>
```